Personal Training Elite Athletes

We are looking for a business card for elite athletic development business called Vanguard Peak. Our ultimate goal is to develop professional athletes. I would like to see the logo be a creative representation of the business name using Metallic Orange (including similar shades) and Silver. I would like the business card to communicate a modern, unique and sport feel.

Industry/Entity Type

Business

```html
<!DOCTYPE html>
<html lang="en">
<head>
<meta charset="utf-8">
<title>Vanguard Peak — Business Card</title>
<link rel="stylesheet" href="https://fonts.googleapis.com/css2?family=Exo+2:wght@400;500&display=swap">
<style>
  :root {
    --backdrop: #e9e6e1;
    --card-black: #050505;
    --card-white: #ffffff;
    --accent-orange: #f0662a;
    --text-light: #f4f4f4;
    --text-grey: #6b6b6b;
  }
  html, body {
    margin: 0;
    padding: 0;
    width: 1200px;
    height: 1085px;
    overflow: hidden;
    background: var(--backdrop);
  }
  .canvas {
    width: 1200px;
    height: 1085px;
    display: flex;
    align-items: center;
    justify-content: center;
  }
  .business-card {
    position: relative;
    width: 1000px;
    height: 572px;
    background: var(--card-white);
    box-shadow: 0 18px 40px rgba(0,0,0,0.25);
    overflow: hidden;
    font-family: "Exo 2", sans-serif;
  }
  .card-dark-panel {
    position: absolute;
    inset: 0;
    width: 100%;
    height: 100%;
  }
  .contact-list {
    position: absolute;
    left: 0;
    top: 0;
    width: 560px;
    height: 100%;
  }
  .contact-row {
    position: absolute;
    right: 0;
    display: flex;
    align-items: center;
    gap: 26px;
  }
  .contact-row--phone { top: 92px; }
  .contact-row--address { top: 228px; }
  .contact-row--web { top: 364px; }
  .contact-text {
    color: var(--text-light);
    font-size: 31px;
    line-height: 1.18;
    letter-spacing: 1.5px;
    text-align: right;
  }
  .contact-icon {
    width: 60px;
    height: 60px;
    flex: none;
  }
  .brand-block {
    position: absolute;
    left: 610px;
    top: 0;
    width: 370px;
    height: 100%;
    display: flex;
    flex-direction: column;
    align-items: center;
    justify-content: center;
  }
  .brand-lockup {
    display: flex;
    align-items: center;
    gap: 14px;
  }
  .brand-square {
    width: 26px;
    height: 26px;
    background: var(--accent-orange);
  }
  .brand-name {
    color: var(--accent-orange);
    font-size: 38px;
    font-weight: 500;
    letter-spacing: 2px;
    white-space: nowrap;
  }
  .brand-tagline {
    margin-top: 10px;
    color: var(--text-grey);
    font-size: 13px;
    letter-spacing: 2px;
    white-space: nowrap;
  }
</style>
</head>
<body>
<main class="canvas">
  <section class="business-card" aria-label="Vanguard Peak business card">
    <svg class="card-dark-panel" viewBox="0 0 1000 572" aria-hidden="true">
      <path fill="var(--card-black)" d="M0 0 H575
        C575 40 560 60 575 80
        C600 95 640 110 630 150
        C620 190 585 195 582 216
        C580 236 640 240 630 286
        C620 330 585 332 582 352
        C580 372 640 378 630 422
        C620 466 575 470 575 510
        V572 H0 Z"/>
    </svg>

    <div class="contact-list">
      <div class="contact-row contact-row--phone">
        <div class="contact-text">020 555 0147<br>020 555 0148</div>
        <svg class="contact-icon" viewBox="0 0 60 60" aria-hidden="true">
          <circle cx="30" cy="30" r="26" fill="none" stroke="var(--accent-orange)" stroke-width="3"/>
          <path d="M22 18 l5 0 l2 7 l-3 3 c2 4 5 7 9 9 l3 -3 l7 2 l0 5 c0 2 -2 3 -4 3 c-12 -1 -21 -10 -22 -22 c0 -2 1 -4 3 -4z" fill="var(--accent-orange)"/>
        </svg>
      </div>
      <div class="contact-row contact-row--address">
        <div class="contact-text">41 7th floor,<br>Harbor Crest Road<br>NVK</div>
        <svg class="contact-icon" viewBox="0 0 60 60" aria-hidden="true">
          <circle cx="30" cy="30" r="26" fill="none" stroke="var(--accent-orange)" stroke-width="3"/>
          <path d="M30 14 c-7 0 -12 5 -12 12 c0 9 12 20 12 20 s12 -11 12 -20 c0 -7 -5 -12 -12 -12z" fill="var(--accent-orange)"/>
          <circle cx="30" cy="26" r="4.5" fill="var(--card-black)"/>
        </svg>
      </div>
      <div class="contact-row contact-row--web">
        <div class="contact-text">coach@vanguardpeak.com<br>vanguardpeak.com</div>
        <svg class="contact-icon" viewBox="0 0 60 60" aria-hidden="true">
          <circle cx="30" cy="30" r="26" fill="none" stroke="var(--accent-orange)" stroke-width="3"/>
          <g fill="none" stroke="var(--accent-orange)" stroke-width="2.4">
            <circle cx="30" cy="30" r="14"/>
            <ellipse cx="30" cy="30" rx="6" ry="14"/>
            <line x1="16" y1="30" x2="44" y2="30"/>
            <line x1="18" y1="23" x2="42" y2="23"/>
            <line x1="18" y1="37" x2="42" y2="37"/>
          </g>
        </svg>
      </div>
    </div>

    <div class="brand-block">
      <div class="brand-lockup">
        <span class="brand-square" aria-hidden="true"></span>
        <span class="brand-name">VANGUARD PEAK</span>
      </div>
      <div class="brand-tagline">TRAIN HARDER · RUN QUICKER · GO FURTHER</div>
    </div>
  </section>
</main>
</body>
</html>
```